Accounting company website and Our Page page design

I need a website designed and copy written for an accounting/bookkeeping company in Ohio. We have content but would need someone to fine-tune it and make it sound good. I also need a Our Page page design created. Attached is the logo for the company.

```html
<!DOCTYPE html>
<html lang="en">
<head>
<meta charset="utf-8">
<title>Meridian Group – Accounting &amp; Bookkeeping</title>
<link href="https://fonts.googleapis.com/css2?family=DM+Serif+Display&family=Lato:wght@400;700;900&display=swap" rel="stylesheet">
<style>
:root{
  --orange:#e9a21b;
  --ink:#2f2f33;
  --text:#4a4a4f;
  --muted:#6b6b70;
  --light:#f2f2f2;
  --white:#ffffff;
  --cta:#3d3e44;
  --footer:#2a2a2c;
  --footer-text:#d8d8d8;
}
*{box-sizing:border-box;margin:0;padding:0}
html,body{width:1200px;height:3795px;overflow:hidden}
body{font-family:"Lato",sans-serif;color:var(--text);background:var(--white);position:relative}
.serif{font-family:"DM Serif Display",serif;font-weight:400}
section,header,footer{position:absolute;left:0;width:1200px}
.abs{position:absolute}
.btn{position:absolute;background:var(--orange);color:var(--white);font-weight:900;text-transform:uppercase;display:flex;align-items:center;justify-content:center;letter-spacing:.3px}
.rule{position:absolute;height:2px;background:var(--orange)}
.section-title{position:absolute;left:0;width:1200px;text-align:center;color:var(--ink);font-size:28px}

/* header */
.site-header{top:0;height:119px}
.brand{position:absolute;left:133px;top:36px;display:flex;align-items:center;gap:10px;font-family:"Lato",sans-serif;font-weight:900;font-size:26px;color:var(--ink);letter-spacing:1px}
.brand .dot{width:22px;height:22px;border-radius:50%;background:var(--orange)}
.follow{position:absolute;left:540px;top:36px;display:flex;align-items:center;gap:10px;font-size:12px;color:var(--ink)}
.soc{width:26px;height:26px;border-radius:50%;background:var(--ink)}
.contact-chip{position:absolute;top:28px;display:flex;gap:10px;align-items:center;font-size:14px;color:var(--ink);line-height:19px}
.chip-icon{width:28px;height:28px;border-radius:50%;background:var(--orange);display:flex;align-items:center;justify-content:center}
.nav{position:absolute;left:540px;top:86px;display:flex;font-size:13px;color:var(--ink)}
.nav span{position:absolute;white-space:nowrap}
.nav .active{color:var(--orange);text-decoration:underline;text-underline-offset:4px}

/* hero */
.hero{top:119px;height:496px}
.hero-photo{position:absolute;inset:0;background:linear-gradient(90deg,#f1f2f3 0%,#e9ebee 35%,#c9ced6 60%,#8e96a2 80%,#5b5f66 100%)}
.hero h1{position:absolute;left:133px;top:72px;font-size:44px;line-height:50px;color:var(--ink)}
.hero p{position:absolute;left:133px;top:198px;font-size:15px;line-height:22px;color:var(--text);width:300px}
.hero .btn{left:133px;top:268px;width:122px;height:43px;font-size:14px}
.dots{position:absolute;left:568px;top:455px;display:flex;gap:8px}
.dots i{width:10px;height:10px;border-radius:50%;border:1.5px solid var(--white)}
.dots i.on{background:var(--orange);border-color:var(--orange)}

/* about */
.about{top:615px;height:585px}
.about-photo{position:absolute;left:130px;top:71px;width:331px;height:457px;background:linear-gradient(160deg,#a57c54,#6b4a30 55%,#8b6a4d)}
.about h2{position:absolute;left:511px;top:84px;font-size:26px;color:var(--ink)}
.about p{position:absolute;left:513px;width:560px;font-size:13px;line-height:19px;color:var(--text)}
.about .btn{left:517px;top:335px;width:87px;height:28px;font-size:10px}
.person{position:absolute;top:408px;display:flex;gap:18px}
.person .ph{width:105px;height:115px;background:linear-gradient(180deg,#cfd3d7,#7d8793)}
.person h4{font-size:13px;font-weight:900;color:var(--ink);margin-top:17px}
.person p{position:static;width:140px;font-size:11.5px;line-height:17px;margin-top:14px;color:var(--muted)}

/* services */
.services{top:1200px;height:574px;background:var(--light)}
.svc-grid{position:absolute;left:113px;top:128px;display:grid;grid-template-columns:repeat(3,321px);column-gap:14px;row-gap:24px}
.svc{height:165px;padding:18px 20px 0 28px;display:flex;gap:18px}
.svc.featured{background:var(--orange)}
.svc svg{flex:none;width:52px;height:52px}
.svc h3{font-size:17px;color:var(--ink);margin-bottom:12px}
.svc p{font-size:12px;line-height:16px;color:var(--muted);width:195px}
.svc.featured h3,.svc.featured p{color:var(--white)}
.services .btn{left:526px;top:504px;width:151px;height:33px;font-size:11px}

/* why */
.why{top:1774px;height:736px}
.why-item{position:absolute;width:200px;text-align:center}
.why-item svg{width:44px;height:44px;display:block;margin:0 auto 8px}
.why-item h4{font-size:15px;color:var(--ink);margin-bottom:10px}
.why-item p{font-size:11px;line-height:16px;color:var(--muted)}
.why-divider{position:absolute;left:350px;top:162px;height:508px;border-left:1px dashed #c8c8c8}
.why-photo{position:absolute;left:630px;top:155px;width:436px;height:524px;background:linear-gradient(180deg,#eef0f2,#d9dde2 40%,#4a5670 75%,#8f949b)}

/* stats */
.stats{top:2510px;height:255px;background:linear-gradient(180deg,#2c2a2a,#3b342d 55%,#232323)}
.stat{position:absolute;top:86px;width:300px;text-align:center;color:var(--white)}
.stat b{display:block;font-family:"DM Serif Display",serif;font-weight:400;font-size:37px;line-height:44px}
.stat span{font-size:16px}

/* testimonials */
.testimonials{top:2765px;height:536px;background:var(--light)}
.t-card{position:absolute;top:155px;width:292px;height:315px;background:var(--white);border-bottom:4px solid var(--orange);text-align:center;padding:30px 36px 0}
.t-card .q{font-family:"DM Serif Display",serif;font-size:30px;color:var(--ink);line-height:30px}
.t-card p{font-size:13px;line-height:19px;color:var(--muted);margin-top:14px}
.t-card hr{width:28px;border:0;border-top:1px solid var(--ink);margin:26px auto 14px}
.t-card h5{font-size:12px;font-weight:900;color:var(--ink)}
.arrow{position:absolute;top:295px}

/* cta */
.cta{top:3301px;height:153px;background:var(--cta);border-bottom:3px solid var(--orange)}
.cta h2{position:absolute;left:131px;top:28px;font-size:25px;color:var(--white)}
.cta p{position:absolute;left:131px;top:64px;font-size:13px;color:#e3e3e3}
.cta .btn{left:131px;top:105px;width:159px;height:47px;font-size:14px;gap:10px}

/* footer */
.site-footer{top:3454px;height:341px;background:var(--footer);color:var(--footer-text)}
.f-brand{position:absolute;left:130px;top:104px;display:flex;align-items:center;gap:10px;font-weight:900;font-size:26px;color:var(--white);letter-spacing:1px}
.f-brand .dot{width:22px;height:22px;border-radius:50%;background:var(--orange)}
.f-head{position:absolute;top:48px;font-size:12px;font-weight:900;color:var(--white);letter-spacing:.5px}
.f-item{position:absolute;display:flex;gap:12px;font-size:11.5px;line-height:15px}
.f-item .ic{flex:none;width:24px;height:24px;border-radius:50%;background:#e6e6e6;display:flex;align-items:center;justify-content:center}
.f-menu{position:absolute;left:789px;top:84px;font-size:11.5px;line-height:24px}
.f-line{position:absolute;left:130px;top:265px;width:940px;border-top:1px solid #444}
.copy{position:absolute;left:0;width:1200px;top:303px;text-align:center;font-size:11px}
</style>
</head>
<body>

<header class="site-header">
  <div class="brand"><span>MERIDIAN GROUP</span><span class="dot"></span></div>
  <div class="follow">Follow <span class="soc"></span><span class="soc"></span><span class="soc"></span></div>
  <div class="contact-chip" style="left:718px">
    <div class="chip-icon"><svg width="14" height="10" viewBox="0 0 14 10"><rect x="1" y="1" width="12" height="8" fill="none" stroke="#fff" stroke-width="1.5"/><path d="M1 1l6 5 6-5" fill="none" stroke="#fff" stroke-width="1.5"/></svg></div>
    <div>Email Us<br>info@meridiangroup.com</div>
  </div>
  <div class="contact-chip" style="left:917px">
    <div class="chip-icon"><svg width="12" height="12" viewBox="0 0 12 12"><path d="M2 1l2.5 0 1 3-1.5 1a7 7 0 003 3l1-1.5 3 1v2.5c-5 .5-9.5-4-9-9z" fill="#fff"/></svg></div>
    <div>Call Us<br>+1 555 014 2290</div>
  </div>
  <nav class="nav">
    <span class="active" style="left:0">HOME</span>
    <span style="left:78px">ABOUT US</span>
    <span style="left:181px">SERVICES</span>
    <span style="left:284px">PRICING</span>
    <span style="left:379px">BLOG</span>
    <span style="left:446px">CONTACT US</span>
  </nav>
</header>

<section class="hero">
  <div class="hero-photo" role="img" aria-label="Woman working with a calculator at a desk with computer monitors showing spreadsheets"></div>
  <h1 class="serif">Accounting<br>&amp; Bookkeeping</h1>
  <p>There are many variations of passages of Lorem Ipsum available but the majority</p>
  <div class="btn">Read More</div>
  <div class="dots"><i></i><i class="on"></i><i></i><i></i></div>
</section>

<section class="about">
  <div class="about-photo" role="img" aria-label="Team reviewing charts and reports around a wooden table with a laptop"></div>
  <div class="rule" style="left:511px;top:68px;width:141px"></div>
  <h2 class="serif">Welcome to Meridian Group</h2>
  <p style="top:131px">There are many variations of passages of Lorem Ipsum available, but the majority have suffered alteration in some form, by injected humour, or randomised words which don't look even slightly believable. If you are going to use a passage of Lorem Ipsum, you need to be sure there isn't anything embarrassing hidden in the middle of text. All the Lorem Ipsum generators on the Internet tend to repeat predefined chunks as necessary,</p>
  <p style="top:252px">Lorem ipsum dolor sit amet, consectetur adipiscing elit, sed do eiusmod tempor incididunt ut labore et dolore magna aliqua. Ut enim ad minim veniam, quis nostrud exercitation ullamco laboris nisi ut aliquip ex ea commodo consequat.</p>
  <div class="btn">Read More</div>
  <div class="person" style="left:515px">
    <div class="ph" role="img" aria-label="Portrait of team member Daniel"></div>
    <div><h4>Daniel</h4><p>Sed ut perspiciatis unde omnis iste natus error sit voluptatem accusantium</p></div>
  </div>
  <div class="person" style="left:811px">
    <div class="ph" role="img" aria-label="Portrait of team member Owen Carter"></div>
    <div><h4>Owen Carter</h4><p>Sed ut perspiciatis unde omnis iste natus error sit voluptatem accusantium</p></div>
  </div>
</section>

<section class="services">
  <div class="rule" style="left:530px;top:54px;width:140px"></div>
  <h2 class="section-title serif" style="top:66px">Our Services</h2>
  <div class="svc-grid">
    <div class="svc">
      <svg viewBox="0 0 52 52" fill="none" stroke="#3a3a3e" stroke-width="1.8"><circle cx="26" cy="18" r="12"/><path d="M29 13h-4a2.5 2.5 0 000 5h2a2.5 2.5 0 010 5h-5M26 10v3M26 23v3"/><path d="M6 40l8-5h10l3 3h-9M6 46l10-2 18-8"/></svg>
      <div><h3 class="serif">Payroll</h3><p>There are many variations of passages of Lorem Ipsum available, but the majority have suffered alteration in some form, by injected humour, or randomised words which don't look.</p></div>
    </div>
    <div class="svc featured">
      <svg viewBox="0 0 52 52" fill="none" stroke="#fff" stroke-width="1.8"><path d="M6 4h26l8 8v36H6z"/><path d="M32 4v8h8"/><text x="9" y="24" font-size="11" fill="#fff" stroke="none" font-family="Lato,sans-serif">TAX</text><rect x="24" y="28" width="22" height="20"/><path d="M28 33h14M28 38h4M34 38h4M28 43h4M34 43h4M11 32h9M11 37h9"/></svg>
      <div><h3 class="serif">Tax Preparation</h3><p>There are many variations of passages of Lorem Ipsum available, but the majority have suffered alteration in some form, by injected humour, or randomised words which don't look.</p></div>
    </div>
    <div class="svc">
      <svg viewBox="0 0 52 52" fill="none" stroke="#3a3a3e" stroke-width="1.8"><circle cx="12" cy="12" r="6"/><circle cx="26" cy="8" r="6"/><circle cx="40" cy="12" r="6"/><circle cx="26" cy="38" r="10"/><path d="M12 18l10 12M26 14v14M40 18l-10 12M28.5 34h-3.5a2 2 0 000 4h2a2 2 0 010 4h-4"/></svg>
      <div><h3 class="serif">Expenses</h3><p>There are many variations of passages of Lorem Ipsum available, but the majority have suffered alteration in some form, by injected humour, or randomised words which don't look.</p></div>
    </div>
    <div class="svc">
      <svg viewBox="0 0 52 52" fill="none" stroke="#3a3a3e" stroke-width="1.8"><path d="M10 4h22l10 10v34H10z"/><path d="M32 4v10h10"/><path d="M30 22h-6a3 3 0 000 6h4a3 3 0 010 6h-7M26 19v3M26 34v3"/></svg>
      <div><h3 class="serif">Invoicing &amp; Payments</h3><p>There are many variations of passages of Lorem Ipsum available, but the majority have suffered alteration in some form, by injected humour, or randomised words which don't look.</p></div>
    </div>
    <div class="svc">
      <svg viewBox="0 0 52 52" fill="none" stroke="#3a3a3e" stroke-width="1.8"><rect x="14" y="4" width="26" height="42" rx="2"/><rect x="18" y="9" width="18" height="8"/><path d="M19 23h4M26 23h4M33 23h2M19 29h4M26 29h4M33 29h2M19 35h4M26 35h4M33 35h2M19 41h4M26 41h4"/><circle cx="10" cy="40" r="6"/></svg>
      <div><h3 class="serif">Accounting</h3><p>There are many variations of passages of Lorem Ipsum available, but the majority have suffered alteration in some form, by injected humour, or randomised words which don't look.</p></div>
    </div>
    <div class="svc">
      <svg viewBox="0 0 52 52" fill="none" stroke="#3a3a3e" stroke-width="1.8"><rect x="4" y="6" width="12" height="40"/><rect x="18" y="6" width="12" height="40"/><rect x="32" y="6" width="12" height="40"/><path d="M7 12h6M7 17h6M21 12h6M21 17h6M35 12h6M35 17h6M22 34h26l-4-4M48 34l-4 4"/></svg>
      <div><h3 class="serif">Bookkeeping</h3><p>There are many variations of passages of Lorem Ipsum available, but the majority have suffered alteration in some form, by injected humour, or randomised words which don't look.</p></div>
    </div>
  </div>
  <div class="btn">View More Services</div>
</section>

<section class="why">
  <div class="rule" style="left:530px;top:66px;width:140px"></div>
  <h2 class="section-title serif" style="top:82px">Why Choose us</h2>
  <div class="why-divider"></div>

  <div class="why-item" style="left:122px;top:159px">
    <svg viewBox="0 0 44 44" fill="none" stroke="#3a3a3e" stroke-width="1.8"><path d="M22 4l15 6v11c0 10-7 16-15 19C14 37 7 31 7 21V10z"/><path d="M15 22l5 5 9-10"/></svg>
    <h4 class="serif">We're Trusted</h4><p>There are many variations of passages of Lorem Ipsum available, but the majority have suffered.</p>
  </div>
  <div class="why-item" style="left:374px;top:159px">
    <svg viewBox="0 0 44 44" fill="none" stroke="#3a3a3e" stroke-width="1.8"><path d="M3 14l8-6 10 4 10-4 10 6-8 12-10 8-12-10z"/><path d="M21 12l-6 6 4 3 6-5M15 28l4 4M19 25l4 4M23 22l4 4"/></svg>
    <h4 class="serif">We're Family Owned</h4><p>There are many variations of passages of Lorem Ipsum available, but the majority have suffered.</p>
  </div>
  <div class="why-item" style="left:122px;top:344px">
    <svg viewBox="0 0 44 44" fill="none" stroke="#3a3a3e" stroke-width="1.8"><path d="M10 4h26v30H6V8a4 4 0 014-4z"/><path d="M13 12h18M13 17h18M13 22h12M26 34v8l4-3 4 3v-8"/></svg>
    <h4 class="serif">We're Certified</h4><p>There are many variations of passages of Lorem Ipsum available, but the majority have suffered.</p>
  </div>
  <div class="why-item" style="left:374px;top:344px">
    <svg viewBox="0 0 44 44" fill="none" stroke="#3a3a3e" stroke-width="1.8"><ellipse cx="22" cy="30" rx="14" ry="10"/><path d="M14 40l1 3M30 40l-1 3M34 26h4v6h-3"/><circle cx="20" cy="10" r="6"/><path d="M18 20h6"/></svg>
    <h4 class="serif">Save Money</h4><p>There are many variations of passages of Lorem Ipsum available, but the majority have suffered.</p>
  </div>
  <div class="why-item" style="left:122px;top:527px">
    <svg viewBox="0 0 44 44" fill="none" stroke="#3a3a3e" stroke-width="1.8"><circle cx="22" cy="24" r="17"/><circle cx="22" cy="24" r="12"/><path d="M22 16v8l5 4M18 4h8"/></svg>
    <h4 class="serif">Save Time</h4><p>There are many variations of passages of Lorem Ipsum available, but the majority have suffered.</p>
  </div>
  <div class="why-item" style="left:374px;top:527px">
    <svg viewBox="0 0 44 44" fill="none" stroke="#3a3a3e" stroke-width="1.8"><path d="M22 34S10 22 10 14a12 12 0 0124 0c0 8-12 20-12 20z"/><circle cx="22" cy="14" r="4"/><ellipse cx="22" cy="38" rx="10" ry="3"/></svg>
    <h4 class="serif">We're Local</h4><p>There are many variations of passages of Lorem Ipsum available, but the majority have suffered.</p>
  </div>

  <div class="why-photo" role="img" aria-label="Smiling accountant in a navy suit seated at a desk with a laptop"></div>
</section>

<section class="stats" role="img" aria-label="Dusk city skyline behind statistics">
  <div class="stat" style="left:59px"><b>100+</b><span>Serving Clients</span></div>
  <div class="stat" style="left:284px"><b>5000+</b><span>Invoices Processing Per Month</span></div>
  <div class="stat" style="left:579px"><b>15000+</b><span>Bank &amp; CC Reconciliation in a Month</span></div>
  <div class="stat" style="left:838px"><b>100+</b><span>Completed Projects</span></div>
</section>

<section class="testimonials">
  <div class="rule" style="left:530px;top:55px;width:140px"></div>
  <h2 class="section-title serif" style="top:80px">Testimonials</h2>
  <svg class="arrow" style="left:76px" width="16" height="24" viewBox="0 0 16 24"><path d="M12 2L3 12l9 10" fill="none" stroke="#555" stroke-width="1.6"/></svg>
  <svg class="arrow" style="left:1107px" width="16" height="24" viewBox="0 0 16 24"><path d="M4 2l9 10-9 10" fill="none" stroke="#555" stroke-width="1.6"/></svg>
  <div class="t-card" style="left:130px"><div class="q">&ldquo;</div><p>But I must explain to you how all this mistaken idea of denouncing pleasure and praising pain was born and I will give you a complete account of the system, and expound the actual teachings of the great explorer of the truth, the ma ster-builder of human.</p><hr><h5>Owen Carter</h5></div>
  <div class="t-card" style="left:454px"><div class="q">&ldquo;</div><p>But I must explain to you how all this mistaken idea of denouncing pleasure and praising pain was born and I will give you a complete account of the system, and expound the actual teachings of the great explorer of the truth, the ma ster-builder of human.</p><hr><h5>Owen Carter</h5></div>
  <div class="t-card" style="left:778px"><div class="q">&ldquo;</div><p>But I must explain to you how all this mistaken idea of denouncing pleasure and praising pain was born and I will give you a complete account of the system, and expound the actual teachings of the great explorer of the truth, the ma ster-builder of human.</p><hr><h5>Owen Carter</h5></div>
</section>

<section class="cta">
  <h2 class="serif">Contact Us For A Free Consultation Today!</h2>
  <p>Call us to learn more about our Bookkeeping, Accounting, Training and Consulting Services.</p>
  <div class="btn"><svg width="18" height="16" viewBox="0 0 18 16"><rect x="2" y="3" width="14" height="11" rx="1" fill="none" stroke="#fff" stroke-width="1.6"/><path d="M5 7h8M5 10h5" stroke="#fff" stroke-width="1.6"/></svg>Contact Us</div>
</section>

<footer class="site-footer">
  <div class="f-brand"><span>MERIDIAN GROUP</span><span class="dot"></span></div>

  <div class="f-head" style="left:434px">CONTACT US</div>
  <div class="f-item" style="left:434px;top:94px"><span class="ic"><svg width="10" height="12" viewBox="0 0 10 12"><path d="M5 11S1 7 1 4.5a4 4 0 018 0C9 7 5 11 5 11z" fill="#2a2a2c"/></svg></span><span>Suite 210, Level 2 West,<br>455 Harbor Lane, Columbus OH 43215.</span></div>
  <div class="f-item" style="left:434px;top:144px"><span class="ic"><svg width="11" height="11" viewBox="0 0 12 12"><path d="M2 1l2.5 0 1 3-1.5 1a7 7 0 003 3l1-1.5 3 1v2.5c-5 .5-9.5-4-9-9z" fill="#2a2a2c"/></svg></span><span>Call Us<br>+1 555 014 2290</span></div>
  <div class="f-item" style="left:434px;top:195px"><span class="ic"><svg width="12" height="9" viewBox="0 0 14 10"><rect x="1" y="1" width="12" height="8" fill="#2a2a2c"/><path d="M1 1l6 5 6-5" fill="none" stroke="#e6e6e6" stroke-width="1.2"/></svg></span><span>E mail Us<br>info@meridiangroup.com</span></div>

  <div class="f-head" style="left:789px">MENU</div>
  <div class="f-menu">HOME<br>ABOUT US<br>SERVICES<br>PRICING<br>BLOG<br>CONTACT US</div>

  <div class="f-head" style="left:966px">FOLLOW US</div>
  <div class="f-item" style="left:966px;top:96px"><span class="ic"></span><span>Like us on<br>OUR PAGE</span></div>
  <div class="f-item" style="left:966px;top:146px"><span class="ic"></span><span>Follow us on<br>NEWSFEED</span></div>
  <div class="f-item" style="left:966px;top:197px"><span class="ic"></span><span>Follow us on<br>NETWORK</span></div>

  <div class="f-line"></div>
  <div class="copy">Copyright © 2022 All Rights Reserved</div>
</footer>

</body>
</html>
```